Bref créative
Valmirock Stationary Design
Business Cards, Letterhead, etc....
Professional
Dorian K. Pelletrow
Chief Executive Officer
2718 N. Birch Ln.
Suite K-42
Tempe, AZ 85107-3318
XXX-XXX-XXXX
dorian@valmirock-example.com
http://www.valmirock-example.com/
See our website for our business areas and marketing information.
Back of the business card should be branded, but simple. Maybe our company monogram. There should be enough space to write notes on the back of the card.
Contains several versions of our logo for stationary design.

```html
<!DOCTYPE html>
<html lang="en">
<head>
<meta charset="utf-8">
<title>Valmirock Stationery Set</title>
<link rel="stylesheet" href="https://fonts.googleapis.com/css2?family=Roboto:wght@400;700&display=swap">
<style>
  :root {
    --teal-deep: #0b5677;
    --teal-mid: #1a7fa3;
    --teal-light: #4fb3d2;
    --paper: #ffffff;
    --ink: #5a6670;
    --ink-light: #9aa4ab;
    --mark-grey: #b9c2c8;
    --ghost: #e6edf1;
  }
  html, body { margin: 0; padding: 0; overflow: hidden; }
  body {
    width: 1200px; height: 785px; position: relative;
    background: var(--paper);
    font-family: "Roboto", Arial, sans-serif;
  }
  .piece { position: absolute; background: var(--paper); box-shadow: 0 1px 4px rgba(0,0,0,.25); }

  .brand { display: flex; align-items: center; gap: 6px; font-weight: 700; color: var(--teal-mid); text-transform: uppercase; letter-spacing: .04em; }
  .brand-dot { border-radius: 50%; background: var(--mark-grey); flex: none; }

  /* Envelope */
  .envelope { left: 36px; top: 173px; width: 372px; height: 120px; }
  .envelope svg { position: absolute; inset: 0; }
  .envelope .brand { position: absolute; left: 262px; top: 18px; font-size: 12px; color: #fff; }
  .envelope .brand-dot { width: 16px; height: 16px; background: #d6dde2; }

  /* Business card */
  .card { left: 36px; top: 312px; width: 372px; height: 211px; }
  .card-panel {
    position: absolute; left: 89px; top: 0; right: 0; bottom: 0;
    background: radial-gradient(ellipse at 45% 10%, var(--teal-light) 0%, var(--teal-mid) 40%, var(--teal-deep) 100%);
  }
  .card .brand { position: absolute; left: 4px; top: 26px; flex-direction: column; gap: 4px; font-size: 11px; }
  .card .brand-dot { width: 28px; height: 28px; }
  .card-contact { position: absolute; left: 210px; bottom: 14px; display: flex; gap: 14px; font-size: 5.5px; line-height: 1.5; color: #dbeef5; }

  /* Letterhead */
  .letterhead { left: 427px; top: 19px; width: 401px; height: 744px; }
  .letterhead > .brand { position: absolute; left: 62px; top: 26px; font-size: 20px; }
  .letterhead > .brand .brand-dot { width: 34px; height: 34px; }
  .letterhead-ghost { position: absolute; left: 266px; top: 548px; width: 140px; height: 140px; border-radius: 50%; background: var(--ghost); }
  .letterhead-footer { position: absolute; left: 26px; right: 20px; bottom: 28px; display: flex; gap: 80px; font-size: 7px; line-height: 1.5; color: var(--ink-light); }

  /* Round sticker */
  .sticker {
    left: 926px; top: 187px; width: 274px; height: 274px; border-radius: 50%;
    background: radial-gradient(circle at 50% 25%, var(--teal-light) 0%, var(--teal-mid) 45%, var(--teal-deep) 100%);
    display: flex; align-items: center; justify-content: center;
  }
  .sticker .brand { flex-direction: column; gap: 14px; font-size: 19px; color: #fff; margin-top: 10px; }
  .sticker .brand-dot { width: 82px; height: 82px; background: #d6dde2; }
</style>
</head>
<body>

  <section class="piece envelope" aria-label="Envelope">
    <svg width="372" height="120" viewBox="0 0 372 120">
      <defs>
        <radialGradient id="envelopeTeal" cx="55%" cy="15%" r="80%">
          <stop offset="0" stop-color="#4fb3d2"/>
          <stop offset=".45" stop-color="#1a7fa3"/>
          <stop offset="1" stop-color="#0b5677"/>
        </radialGradient>
      </defs>
      <path d="M96 0 H372 V56 C300 60 200 62 120 56 C104 40 98 20 96 0 Z" fill="url(#envelopeTeal)"/>
    </svg>
    <div class="brand"><span class="brand-dot"></span></div>
  </section>

  <section class="piece card" aria-label="Business card">
    <div class="card-panel"></div>
    <div class="brand"><span class="brand-dot"></span>Valmirock</div>
    <div class="card-contact">
      <div>Address:<br>2718 N. Birch Ln.<br>Tempe, AZ 85107-3318</div>
      <div>Phone: XXX-XXX-XXXX<br>Email: dorian@valmirock-example.com<br>Web: www.valmirock-example.com</div>
    </div>
  </section>

  <section class="piece letterhead" aria-label="Letterhead">
    <div class="brand"><span class="brand-dot"></span>Valmirock</div>
    <div class="letterhead-ghost" role="img" aria-label="Faint brand circle"></div>
    <div class="letterhead-footer">
      <div>Address:<br>2718 N. Birch Ln. Tempe, AZ 85107-3318</div>
      <div>Phone: XXX-XXX-XXXX<br>Email: dorian@valmirock-example.com<br>Web: www.valmirock-example.com</div>
    </div>
  </section>

  <section class="piece sticker" aria-label="Round sticker">
    <div class="brand"><span class="brand-dot"></span>Valmirock</div>
  </section>

</body>
</html>
```